Industrial Rubber Catalogue Redesign, Rebranded

We have rececntly merged with one of our suppliers KVR Maritime, we were formally known as Brightvale Castings & Seals, our new name is KVR Brightvale Castings and are needing to refresh the current catalogue, front page and header and footer template of the product pages.
Looking for a professional clean look, i have attached our new letterhead, current catalogue and some logos, for the next year we will have 2 logos and will create a new logo in 2019.

Target Market(s)

Caravan, Camper Trailers, Ute Tollbox Manufactures, Enginerering workshops

Industry/Entity Type

Industrial

Font styles to use
Sans Serif

Colors

Designer to choose colors to be used in the design.

Requirements
Must have
• Clean new look
Nice to have
• I have added a new image for profiles to try to add to the front cover design, would like to keep the others and make it work somehow

```html
<!DOCTYPE html>
<html lang="en">
<head>
<meta charset="utf-8">
<title>Industrial Range 2015 — KVR Brightvale Castings</title>
<link rel="stylesheet" href="https://fonts.googleapis.com/css2?family=Inter:wght@400;700;800&display=swap">
<style>
  :root {
    --brand-blue: #0a7fc9;
    --poly-light: #eceded;
    --poly-mid: #c9cacb;
    --poly-dark: #a9aaab;
    --rubber-light: #55585c;
    --rubber-dark: #2e3033;
    --paper: #ffffff;
    --ink: #111111;
  }
  html, body {
    margin: 0;
    padding: 0;
    overflow: hidden;
  }
  body {
    width: 848px;
    height: 1200px;
    background: var(--paper);
  }
  .cover {
    position: relative;
    width: 848px;
    height: 1200px;
    overflow: hidden;
    font-family: "Inter", Arial, sans-serif;
  }
  .cover__art {
    position: absolute;
    inset: 0;
  }
  .cover__title {
    position: absolute;
    left: 80px;
    top: 70px;
    margin: 0;
    color: var(--paper);
    font-weight: 800;
    font-size: 45px;
    line-height: 44px;
    letter-spacing: -0.5px;
  }
  .cover__year {
    display: block;
    font-size: 76px;
    line-height: 80px;
    letter-spacing: -1px;
  }
  .brand-bar {
    position: absolute;
    left: 470px;
    top: 1060px;
    width: 360px;
    height: 90px;
    display: flex;
    align-items: center;
    gap: 24px;
    color: var(--ink);
    font-weight: 700;
  }
  .brand-bar__name {
    font-size: 19px;
    line-height: 22px;
    letter-spacing: 0.5px;
    text-transform: uppercase;
  }
  .brand-bar__partner {
    display: flex;
    align-items: center;
    gap: 8px;
    font-size: 19px;
    line-height: 22px;
    text-transform: uppercase;
  }
  .brand-bar__dot {
    width: 16px;
    height: 16px;
    border-radius: 50%;
    background: var(--brand-blue);
    flex: none;
  }
</style>
</head>
<body>
<main class="cover">
  <svg class="cover__art" width="848" height="1200" viewBox="0 0 848 1200">
    <defs>
      <linearGradient id="polyGrey" x1="0" y1="0" x2="1" y2="1">
        <stop offset="0" stop-color="var(--poly-light)"/>
        <stop offset="0.5" stop-color="var(--poly-mid)"/>
        <stop offset="1" stop-color="var(--poly-dark)"/>
      </linearGradient>
      <linearGradient id="rubberTone" x1="0" y1="0" x2="1" y2="1">
        <stop offset="0" stop-color="var(--rubber-light)"/>
        <stop offset="1" stop-color="var(--rubber-dark)"/>
      </linearGradient>
    </defs>
    <g role="img" aria-label="Faceted grey low-poly background">
      <rect width="848" height="1200" fill="url(#polyGrey)"/>
    </g>
    <polygon class="blue-field" points="0,0 710,0 330,330 0,268" fill="var(--brand-blue)"/>
    <polygon class="blue-stripe" points="370,1200 848,855 848,885 410,1200" fill="var(--brand-blue)"/>
    <polygon class="footer-field" points="410,1200 848,885 848,1200" fill="var(--paper)"/>

    <path class="product-photo" role="img" aria-label="Photo of sponge rubber D-profile seals with red adhesive tape"
          d="M380,0 H848 V110 L630,330 V625 H355 L0,330 V265 H380 Z" fill="url(#rubberTone)"/>
    <path class="product-photo" role="img" aria-label="Photo of textured edge trim and bulb edge trim seal profiles"
          d="M0,495 L290,700 V960 H180 L0,760 Z" fill="url(#rubberTone)"/>
    <path class="product-photo" role="img" aria-label="Photo of edge trim profiles with top and side bulb seals"
          d="M848,440 V990 H600 V610 Z" fill="url(#rubberTone)"/>
  </svg>

  <h1 class="cover__title">INDUSTRIAL<br>RANGE<span class="cover__year">2015</span></h1>

  <footer class="brand-bar">
    <span class="brand-bar__name">Brightvale<br>Castings &amp; Seals</span>
    <span class="brand-bar__partner"><span class="brand-bar__dot"></span>KVR<br>Maritime</span>
  </footer>
</main>
</body>
</html>
```